Antibacterial Hand Wash Squeeze Tube Label

We're looking for a contemporary label design for a new Antibacterial Hand Wash for an 8oz squeeze tube. The new consumer brand will be sold to consumers in major US retail stores & online. The moisturizing hand wash contains Aloe Vera, vitamin E, and other natural ingredients so the design should include the color green. Real photos are very effective on packaging, so a picture of Aloe Vera or possibly two hands washing would help draw consumers' attention to the tube on the retail shelf. The front label may wrap around the sides. Rear must be left mostly blank
Target Market(s)
US Consumers - retail stores & online
Industry/Entity Type
Consumer

```html
<!DOCTYPE html>
<html lang="en">
<head>
<meta charset="UTF-8">
<title>Verdell Antibacterial Hand Wash Label</title>
<link href="https://fonts.googleapis.com/css2?family=Mulish:wght@400;600;800&display=swap" rel="stylesheet">
<style>
  :root {
    --brand-green: #248a0a;
    --badge-green: #2f8f1c;
    --copy-green: #3c9a1f;
    --ink: #2a2a2a;
    --label-white: #f4f4f4;
    --label-fade: #e6e6e6;
    --backdrop: #e9e9ea;
    --aloe-light: #7cc24a;
    --aloe-dark: #2f7d1f;
  }
  * { margin: 0; padding: 0; box-sizing: border-box; }
  html, body {
    width: 1200px;
    height: 1147px;
    overflow: hidden;
    background: var(--backdrop);
    font-family: "Mulish", sans-serif;
  }
  .label {
    position: absolute;
    left: 401px;
    top: 33px;
    width: 398px;
    height: 1080px;
    background: linear-gradient(180deg, var(--label-white) 0%, var(--label-white) 70%, var(--label-fade) 100%);
    box-shadow: 0 2px 10px rgba(0,0,0,0.08);
  }
  .brand-band {
    position: absolute;
    left: 0; top: 0;
    width: 100%;
    height: 356px;
    background: var(--brand-green);
    display: flex;
    align-items: center;
    justify-content: center;
  }
  .brand-name {
    font-family: "Mulish", sans-serif;
    font-weight: 400;
    font-size: 76px;
    color: #ffffff;
    letter-spacing: -1px;
    margin-top: 20px;
  }
  .product-title {
    position: absolute;
    top: 384px;
    width: 100%;
    text-align: center;
    color: var(--ink);
    font-weight: 400;
    line-height: 1.05;
  }
  .product-title .line-1 { display: block; font-size: 37px; }
  .product-title .line-2 { display: block; font-size: 48px; }
  .aloe-visual {
    position: absolute;
    left: 28px;
    top: 492px;
    width: 328px;
    height: 306px;
    display: block;
  }
  .claim-badge {
    position: absolute;
    left: 57px;
    top: 835px;
    width: 281px;
    height: 67px;
    border: 1.5px solid var(--badge-green);
    border-radius: 8px;
    display: flex;
    overflow: hidden;
    background: #ffffff;
  }
  .claim-badge .percent {
    width: 93px;
    background: var(--badge-green);
    color: #ffffff;
    font-weight: 800;
    font-size: 36px;
    display: flex;
    align-items: center;
    justify-content: center;
  }
  .claim-badge .claim-text {
    flex: 1;
    display: flex;
    flex-direction: column;
    justify-content: center;
    align-items: center;
    color: var(--ink);
    line-height: 1.05;
  }
  .claim-text .claim-top { font-size: 25px; font-weight: 400; }
  .claim-text .claim-bottom { font-size: 23px; font-weight: 800; }
  .ingredients {
    position: absolute;
    top: 932px;
    width: 100%;
    text-align: center;
    color: var(--copy-green);
    font-size: 18.5px;
    line-height: 1.3;
  }
  .net-weight {
    position: absolute;
    top: 1000px;
    width: 100%;
    text-align: center;
    color: var(--ink);
    font-size: 18.5px;
  }
</style>
</head>
<body>
  <main class="label">
    <header class="brand-band">
      <span class="brand-name">Verdell</span>
    </header>

    <h1 class="product-title">
      <span class="line-1">ANTIBACTERIAL</span>
      <span class="line-2">HAND WASH</span>
    </h1>

    <svg class="aloe-visual" role="img" aria-label="Photo of a green aloe vera plant with a gel splash" viewBox="0 0 328 306">
      <defs>
        <radialGradient id="aloeTone" cx="50%" cy="60%" r="55%">
          <stop offset="0%" stop-color="var(--aloe-light)"/>
          <stop offset="70%" stop-color="var(--aloe-dark)" stop-opacity="0.55"/>
          <stop offset="100%" stop-color="var(--aloe-dark)" stop-opacity="0"/>
        </radialGradient>
      </defs>
      <rect width="328" height="306" fill="url(#aloeTone)"/>
    </svg>

    <div class="claim-badge">
      <span class="percent">80%</span>
      <span class="claim-text">
        <span class="claim-top">ALCOHOL</span>
        <span class="claim-bottom">ANTISEPTIC</span>
      </span>
    </div>

    <p class="ingredients">Contains Aloe Vera, vitamin E,<br>and other natural ingredients</p>
    <p class="net-weight">NET WEIGHT: 8OZ</p>
  </main>
</body>
</html>
```